Brenmoor Group needs a business card

I would like the card to be simple but modern and elegant.
I like black and white.
or black and gold.
we are a private finance lender and also are involved in property and property developments.

please look at the business card photos i provided i would like B.G only one one side and all the other details on the other side use fonts that tie in with my theme.

Industry/Entity Type

Finance

Contact Information for Business Card

Brenmoor Group (B.G) Callum Brenmoor M: 0418396152 E: callumbren@quivomail.com

Font styles to use
Other font styles liked:
• Use fonts that would reflect our business

Colors
000000
ffffff

Requirements
Must have
• one side of details
• other side has either B.G or Brenmoor Group like in the photos provided

```html
<!DOCTYPE html>
<html lang="en">
<head>
<meta charset="utf-8">
<title>Brenmoor Group – Business Card</title>
<link rel="stylesheet" href="https://fonts.googleapis.com/css2?family=Poppins:wght@400;600;700&display=swap">
<style>
  :root {
    --black: #000000;
    --white: #ffffff;
    --ink: #111111;
    --charcoal: #2a2a2a;
    --graphite: #3c3c3c;
    --slate: #5a5a5a;
    --silver: #c8c8c8;
    --stage: #e6e6e8;
  }
  * { margin: 0; padding: 0; box-sizing: border-box; }
  html, body {
    width: 1200px;
    height: 800px;
    overflow: hidden;
    background: var(--stage);
    font-family: "Poppins", sans-serif;
  }
  .card-sheet {
    position: relative;
    width: 1200px;
    height: 800px;
    display: flex;
    align-items: center;
    justify-content: center;
    gap: 40px;
  }
  .card {
    position: relative;
    width: 520px;
    height: 300px;
    overflow: hidden;
    box-shadow: 0 10px 30px rgba(0,0,0,0.25);
  }
  .card-art { position: absolute; inset: 0; display: block; }

  /* Front: brand name */
  .card-front .brand-name {
    position: absolute;
    left: 0; right: 0;
    top: 126px;
    text-align: center;
    color: var(--white);
    font-weight: 600;
    font-size: 34px;
    letter-spacing: 1px;
  }

  /* Back: monogram + details */
  .monogram {
    position: absolute;
    left: 0; top: 16px;
    width: 230px; height: 200px;
    display: flex;
    align-items: center;
    justify-content: center;
    font-weight: 700;
    font-size: 84px;
    color: var(--ink);
    letter-spacing: 2px;
  }
  .detail {
    position: absolute;
    left: 290px;
    color: var(--ink);
    font-size: 15px;
    line-height: 1;
  }
  .detail-name { top: 32px; font-weight: 700; font-size: 21px; }
  .detail-role { top: 58px; font-size: 10px; color: var(--graphite); }
  .detail-phone { top: 118px; }
  .detail-email { top: 184px; }
  .detail-address { top: 250px; }
</style>
</head>
<body>
<main class="card-sheet">

  <section class="card card-front" aria-label="Card front">
    <svg class="card-art" viewBox="0 0 520 300" aria-hidden="true">
      <rect width="520" height="300" fill="var(--black)"/>
      <rect x="0" y="12" width="520" height="88" fill="var(--white)"/>
      <rect x="0" y="100" width="110" height="185" fill="var(--ink)"/>
      <rect x="410" y="100" width="110" height="185" fill="var(--ink)"/>
      <rect x="0" y="160" width="70" height="125" fill="var(--charcoal)"/>
      <rect x="450" y="160" width="70" height="125" fill="var(--charcoal)"/>
      <polygon points="110,100 410,100 430,150 410,200 110,200 90,150" fill="var(--charcoal)"/>
      <polygon points="120,206 400,206 420,226 100,226" fill="var(--white)"/>
      <rect x="0" y="286" width="520" height="14" fill="var(--white)"/>
    </svg>
    <p class="brand-name">Brenmoor Group</p>
  </section>

  <section class="card card-back" aria-label="Card back">
    <svg class="card-art" viewBox="0 0 520 300" aria-hidden="true">
      <rect width="520" height="300" fill="var(--silver)"/>
      <rect x="0" y="0" width="520" height="16" fill="var(--black)"/>
      <rect x="0" y="84" width="520" height="18" fill="var(--graphite)"/>
      <rect x="0" y="150" width="520" height="18" fill="var(--graphite)"/>
      <rect x="0" y="216" width="520" height="18" fill="var(--graphite)"/>
      <rect x="0" y="282" width="520" height="18" fill="var(--black)"/>
      <rect x="0" y="16" width="230" height="200" fill="var(--white)"/>
      <rect x="230" y="16" width="48" height="266" fill="var(--slate)"/>
      <!-- person -->
      <g fill="var(--black)">
        <circle cx="254" cy="40" r="7"/>
        <path d="M241 62 Q241 49 254 49 Q267 49 267 62 Z"/>
      </g>
      <!-- phone -->
      <g fill="none" stroke="var(--black)" stroke-width="2.2" stroke-linecap="round" stroke-linejoin="round">
        <path d="M244 118 Q254 110 264 118"/>
        <rect x="245" y="121" width="18" height="12" rx="2"/>
        <circle cx="254" cy="127" r="2.5"/>
      </g>
      <!-- envelope -->
      <g fill="none" stroke="var(--black)" stroke-width="2.2" stroke-linejoin="round">
        <rect x="243" y="184" width="22" height="15"/>
        <path d="M243 184 L254 193 L265 184"/>
      </g>
      <!-- home -->
      <g fill="none" stroke="var(--black)" stroke-width="2.2" stroke-linejoin="round">
        <path d="M243 257 L254 247 L265 257"/>
        <path d="M246 255 L246 267 L262 267 L262 255"/>
        <rect x="251" y="260" width="6" height="7"/>
      </g>
    </svg>
    <div class="monogram">B.G</div>
    <p class="detail detail-name">Callum Brenmoor</p>
    <p class="detail detail-role">Position/ Title</p>
    <p class="detail detail-phone">0418396152</p>
    <p class="detail detail-email">callumbren@quivomail.com</p>
    <p class="detail detail-address">physical address</p>
  </section>

</main>
</body>
</html>
```